Business Card Design Project

We are an agricultural business based in Brisbane.
We design, manage and operate regional saleyards. Our logo is green/silver in colour and details of our business can be found on our website www.vodemarketyards.com.au

Just wanting a corporate design for some business cards and include name, position, contact details.

Thanks

Industry/Entity Type

Business

```html
<!DOCTYPE html>
<html lang="en">
<head>
<meta charset="utf-8">
<title>Vode Market Yards – Business Card</title>
<link rel="stylesheet" href="https://fonts.googleapis.com/css2?family=Ubuntu:ital,wght@0,400;0,700;1,500&display=swap">
<style>
  :root {
    --paper: #ffffff;
    --band-grey: #808080;
    --rule-grey: #d3dcda;
    --contact-bg: #d6dfdd;
    --brand-green: #00c000;
    --text-green: #1db915;
    --ink: #111111;
    --title-light: #e6e6e6;
  }
  html, body {
    margin: 0;
    padding: 0;
    width: 1200px;
    height: 734px;
    overflow: hidden;
    background: var(--paper);
  }
  .card {
    position: relative;
    width: 1200px;
    height: 734px;
    background: var(--paper);
    font-family: "Ubuntu", sans-serif;
    overflow: hidden;
  }
  .card-shapes {
    position: absolute;
    inset: 0;
  }
  .brand-name {
    position: absolute;
    left: 60px;
    top: 82px;
    width: 530px;
    margin: 0;
    text-align: center;
    font-family: "Ubuntu", sans-serif;
    font-weight: 700;
    font-size: 54px;
    line-height: 58px;
    letter-spacing: 1px;
    color: var(--ink);
  }
  .person {
    position: absolute;
    right: 48px;
    top: 306px;
    text-align: right;
  }
  .person-name {
    margin: 0;
    font-family: "Ubuntu", sans-serif;
    font-style: italic;
    font-weight: 500;
    font-size: 60px;
    line-height: 66px;
    letter-spacing: 2px;
    color: #ffffff;
    text-shadow:
      -2px -2px 0 #3a3a3a, 2px -2px 0 #3a3a3a,
      -2px 2px 0 #3a3a3a, 2px 2px 0 #3a3a3a,
      0 2px 0 #3a3a3a, 0 -2px 0 #3a3a3a,
      2px 0 0 #3a3a3a, -2px 0 0 #3a3a3a;
  }
  .person-title {
    margin: 6px 0 0;
    font-family: "Ubuntu", sans-serif;
    font-weight: 400;
    font-size: 32px;
    letter-spacing: 2px;
    color: var(--title-light);
  }
  .contact-list {
    position: absolute;
    left: 52px;
    top: 500px;
    margin: 0;
    padding: 0;
    list-style: none;
  }
  .contact-item {
    display: flex;
    align-items: center;
    height: 60px;
    font-size: 34px;
    letter-spacing: 1.5px;
    color: var(--text-green);
  }
  .contact-icon {
    width: 64px;
    height: 46px;
    margin-right: 16px;
    flex: none;
  }
  .website {
    position: absolute;
    right: 46px;
    top: 652px;
    display: flex;
    align-items: center;
    font-size: 33px;
    letter-spacing: 1.5px;
    color: #ffffff;
  }
  .website-icon {
    width: 60px;
    height: 60px;
    margin-right: 20px;
  }
</style>
</head>
<body>
<div class="card">
  <svg class="card-shapes" width="1200" height="734" viewBox="0 0 1200 734" aria-hidden="true">
    <!-- header band with downward notch -->
    <polygon points="0,257 322,296 587,257 1200,257 1200,472 0,472" fill="var(--rule-grey)"/>
    <polygon points="0,269 322,308 587,269 1200,269 1200,472 0,472" fill="var(--band-grey)"/>
    <!-- band shadow -->
    <rect x="0" y="472" width="1200" height="6" fill="#b9c2c0"/>
    <!-- contact strip -->
    <rect x="0" y="478" width="1200" height="148" fill="var(--contact-bg)"/>
    <rect x="0" y="626" width="1200" height="4" fill="#ffffff"/>
    <!-- footer band -->
    <rect x="0" y="630" width="1200" height="104" fill="var(--brand-green)"/>
  </svg>

  <h1 class="brand-name">VODE MARKET<br>YARDS</h1>

  <div class="person">
    <p class="person-name">Daniel Hartigan</p>
    <p class="person-title">Chief Executive Officer</p>
  </div>

  <ul class="contact-list">
    <li class="contact-item">
      <svg class="contact-icon" viewBox="0 0 64 46" aria-hidden="true">
        <rect x="1" y="5" width="60" height="36" fill="var(--text-green)"/>
        <polyline points="1,5 31,27 61,5" fill="none" stroke="var(--contact-bg)" stroke-width="3"/>
        <line x1="1" y1="41" x2="24" y2="22" stroke="var(--contact-bg)" stroke-width="3"/>
        <line x1="61" y1="41" x2="38" y2="22" stroke="var(--contact-bg)" stroke-width="3"/>
      </svg>
      daniel@vodemarketyards.com.au
    </li>
    <li class="contact-item">
      <svg class="contact-icon" viewBox="0 0 64 60" style="height:60px" aria-hidden="true">
        <g transform="rotate(28 28 34)">
          <rect x="16" y="10" width="24" height="46" rx="4" fill="var(--text-green)"/>
          <rect x="20" y="15" width="16" height="12" fill="var(--contact-bg)"/>
          <g fill="var(--contact-bg)">
            <rect x="20" y="31" width="4" height="4"/><rect x="26" y="31" width="4" height="4"/><rect x="32" y="31" width="4" height="4"/>
            <rect x="20" y="37" width="4" height="4"/><rect x="26" y="37" width="4" height="4"/><rect x="32" y="37" width="4" height="4"/>
            <rect x="20" y="43" width="4" height="4"/><rect x="26" y="43" width="4" height="4"/><rect x="32" y="43" width="4" height="4"/>
          </g>
          <rect x="34" y="2" width="3" height="9" fill="var(--text-green)"/>
        </g>
        <path d="M46 8 a6 6 0 0 1 6 6" fill="none" stroke="var(--text-green)" stroke-width="2"/>
        <path d="M46 3 a11 11 0 0 1 11 11" fill="none" stroke="var(--text-green)" stroke-width="2"/>
      </svg>
      0412 555 019
    </li>
  </ul>

  <div class="website">
    <svg class="website-icon" viewBox="0 0 60 60" aria-hidden="true">
      <g fill="none" stroke="#ffffff" stroke-width="3.5">
        <circle cx="30" cy="30" r="26"/>
        <ellipse cx="30" cy="30" rx="11" ry="26"/>
        <line x1="30" y1="4" x2="30" y2="56"/>
        <line x1="4" y1="30" x2="56" y2="30"/>
        <line x1="8" y1="17" x2="52" y2="17"/>
        <line x1="8" y1="43" x2="52" y2="43"/>
      </g>
    </svg>
    www.vodemarketyards.com.au
  </div>
</div>
</body>
</html>
```